Kelvanta (www.kelvanta.net) needs exciting professional PowerPoint pitch template

Kelvanta is an exciting new start-up targeting innovative ways to engage with retail customers at the point of sale.

Our customers are looking for us to help them increase the "wallet share" of their retail customers. The retail customer has their wallet open at the Point of Sale and are paying money to our customer. At Kelvanta we are all about attracting the attention of the retail customer AT THAT POINT IN TIME and engaging the retail customer in spending a little more in that store or another store that has a relationship to the retail customer's purchase.

Our customers are the owners of very large supermarkets, chain stores, and financial institutions, and therefore when we pitch a proposal to these buyers it needs to be slick, professional, and very memorable.

The PowerPoint sales presentation template is a key part of striking that impression.

Here is some background...

Our Vision
Through applying new thinking to a mature industry we are reinventing selected segments of the Australian retail messaging business, generating significant value for our customers, our suppliers, and our owners.
We operate with integrity, agility, and intelligence to doing things smarter, faster and more efficiently.
We bring deep industry expertise, deep relationships with customers and suppliers, and a will to see the old ways give way to smarter ways – this is why we win.
From this economically sustainable platform, we will examine the disruption of other market segments by further leveraging the elements that make us successful.

Our Values
With our clients, with our suppliers, with our staff, and with our owners:
# We Partner – We align the interest of all stakeholders by striving to ensure everything we do is mutually beneficial and commercially sustainable in the long term. We are clear with all our stakeholders about what our expectations are of them, and we seek clarity from them in their expectations of us.
# We Innovate – In the segments we choose to compete in, we bring fresh ideas, new business processes, the right relationships, and the right technology to ensure the supply chain is nimble, competitive, and reliable.
# We are Accountable – We say what we will do, and then do what we say.
# We Perform – We use our skills, relationships, and reputation to deliver value to our customers, suppliers, and owners.

Initially we are building our business from low-tech through printing promotional offers and retailer messages on ATM and EFTPOS receipts, but as soon as cash flow supports it we will be engaging in high-tech real-time targeted offers to the specific consumer through video wall offers as people are at the checkout or walking through the shopping centre.

I'd like the PowerPoint template to reflect our vision and values.

The PowerPoint template will be used in communicating our proposals to our clients, and needs to catch and hold our audiences attention.

Please check out the web site we have just launched - it is pretty basic but it has only been up a week. We intend to sharpen it over the coming weeks, but you'll get the idea of what our core messages are.

I have recently sourced a logo from ArtHarbor, plus business cards, and have attached the source files for your reference.
Updates

Hi everybody.  Thanks for the designs submitted so far.  Your submissions have helped me understand what I do and don't prefer, and I have updated the "Must Have/Nice to Have/Shouldn't Have" criteria accordingly.  I have also uploaded a powerpoint template that I had at a company I udsed to run that has the sort of visual theme I find appealing. I have more time to provide feedback now that the week is over, so I will comment on individual designs shortly, and I will respond to queries directed to me.

Kind Regards - Grant

Target Market(s)

Our customers are large corporations that have professional Point Of Sale marketing experts looking for a supplier with an edge over others in a crowded market. The buyer of our product and services is ultimately a communications expert. They want to see distinctive competence, and an agility of thinking that will make them money through driving more consumer spending.

Industry/Entity Type

Financial

Font styles to use
Sans Serif

Colors
34a7d7
0892cd
3276b5

Requirements
Must have
• The following Slides: Title Slide, Agenda, About Kelvanta, Thank you
The pages must be easy on the eye.
The final product must be a PowerPoint template file with the usual "Title", "Title and Content", "Title & Table", and "Blank" page types.
Widescreen format please.
Nice to have
• The pages should have an eye-catching visual element running through all the pages. I have attached a template from a company i used to be involved with that has a visual theme running through it that I like.
Plenty of whitespace - have a look at www.kelvanta.net.
Bonus points for pulling the text from the brief into the template.
Use "Innovation - Integrity - Service" as the tag line.
Should not have
• Pages should not be busy.
Stay away from too much black. I know the cards have black, but the presentation shouldn't.
I dont like serifed fonts. Use Dravelle's Modern UI style for insporation.
The "Bringing Lumora" tag line was an invention of the logo designer that we do not want to cary forward. Please do not use it.

```html
<!DOCTYPE html>
<html lang="en">
<head>
<meta charset="utf-8">
<title>Kelvanta Presentation Template</title>
<link rel="stylesheet" href="https://fonts.googleapis.com/css2?family=Exo+2:wght@500;600&family=Ubuntu:wght@400;500;700&display=swap">
<style>
  :root {
    --brand-blue: #0a7cc4;
    --icon-grey: #808184;
    --body-text: #4a4a4c;
    --frame: #3a3a3a;
    --paper: #ffffff;
    --photo-light: #dfe7e6;
    --photo-mid: #b9c6c2;
    --photo-warm: #d8c9a8;
  }
  * { box-sizing: border-box; margin: 0; padding: 0; }
  html, body { width: 1200px; height: 1002px; overflow: hidden; background: var(--paper); }
  body { position: relative; font-family: "Ubuntu", Arial, sans-serif; color: var(--body-text); }

  .slide { position: absolute; background: var(--paper); border: 1px solid var(--frame); overflow: hidden; }
  .slide--title   { left: 77px;  top: 18px;  width: 495px; height: 313px; }
  .slide--agenda  { left: 615px; top: 18px;  width: 496px; height: 314px; }
  .slide--about   { left: 73px;  top: 339px; width: 497px; height: 313px; }
  .slide--content { left: 615px; top: 339px; width: 496px; height: 313px; }
  .slide--blank   { left: 73px;  top: 663px; width: 497px; height: 314px; }
  .slide--thanks  { left: 615px; top: 663px; width: 496px; height: 314px; }

  .heading { position: absolute; left: 49px; top: 13px; font-family: "Exo 2", Arial, sans-serif; font-weight: 500; font-size: 24px; color: var(--brand-blue); letter-spacing: 0.3px; white-space: nowrap; }
  .subheading { position: absolute; left: 49px; top: 39px; font-size: 10px; font-weight: 500; color: #222; }

  .footer { position: absolute; left: 0; right: 0; bottom: 0; height: 25px; background: var(--brand-blue); color: #fff; }
  .footer__brand { position: absolute; left: 50px; top: 5px; font-family: "Ubuntu", Arial, sans-serif; font-weight: 700; font-size: 13px; letter-spacing: -0.3px; }
  .footer__url { position: absolute; right: 40px; top: 5px; font-size: 12px; font-weight: 500; }

  .photo { position: absolute; left: 0; right: 0; }
  .photo--checkout { top: 0; height: 184px; background: linear-gradient(100deg, var(--photo-light) 0%, var(--photo-warm) 35%, var(--photo-mid) 60%, #e9eef0 100%); }
  .photo-rule { position: absolute; left: 0; right: 0; top: 184px; height: 2px; background: var(--brand-blue); }
  .photo--scanner { top: 163px; bottom: 0; background: linear-gradient(180deg, #cfd6d4 0%, #aebab6 45%, #e7e2da 100%); }

  .title-slide__title { position: absolute; left: 57px; top: 228px; font-family: "Exo 2", Arial, sans-serif; font-weight: 500; font-size: 31px; color: var(--brand-blue); }
  .title-slide__brand { position: absolute; left: 355px; top: 241px; font-weight: 700; font-size: 17px; color: var(--brand-blue); letter-spacing: -0.4px; }

  .agenda-item { position: absolute; width: 200px; }
  .agenda-item__title { position: relative; padding-left: 15px; font-size: 10.5px; font-weight: 500; color: #222; line-height: 12px; }
  .agenda-item__num { position: absolute; left: 0; top: 0; width: 11px; height: 11px; border-radius: 50%; background: var(--brand-blue); color: #fff; font-size: 8px; font-weight: 700; text-align: center; line-height: 11px; }
  .agenda-item ul { list-style: none; padding-left: 16px; }
  .agenda-item li { font-size: 8px; line-height: 9.6px; color: var(--body-text); }
  .agenda-item li::before { content: "· "; }
  .agenda-item--muted .agenda-item__title { color: #8a8a8a; }
  .agenda-note { position: absolute; left: 50px; top: 262px; width: 400px; font-size: 6px; line-height: 7.5px; color: #333; }

  .about__mark { position: absolute; left: 48px; top: 138px; }
  .about__text { position: absolute; left: 168px; top: 87px; width: 292px; font-size: 8.2px; font-weight: 500; line-height: 9.6px; color: var(--body-text); }
  .about__text p + p { margin-top: 9px; }

  .feature-icon { position: absolute; top: 79px; width: 98px; height: 98px; border-radius: 50%; }
  .feature-icon--team { left: 47px; background: var(--icon-grey); }
  .feature-icon--idea { left: 197px; background: var(--brand-blue); }
  .feature-icon--process { left: 339px; width: 108px; height: 108px; top: 73px; background: var(--brand-blue); }
  .feature-text { position: absolute; top: 196px; width: 128px; font-size: 8px; font-weight: 500; line-height: 9.6px; color: var(--body-text); }

  .profile-photo { position: absolute; top: 76px; width: 124px; height: 124px; border-radius: 50%; background: radial-gradient(circle at 50% 62%, var(--brand-blue) 0 38%, var(--icon-grey) 39%); }
  .profile-text { position: absolute; top: 205px; width: 198px; font-size: 8px; font-weight: 500; line-height: 9.8px; color: var(--body-text); }

  .thanks__title { position: absolute; left: 0; right: 0; top: 85px; text-align: center; font-family: "Exo 2", Arial, sans-serif; font-weight: 500; font-size: 24px; color: var(--brand-blue); }
  .thanks__url { position: absolute; left: 0; right: 0; top: 132px; text-align: center; font-size: 12px; font-weight: 500; color: var(--brand-blue); }
</style>
</head>
<body>

<section class="slide slide--title">
  <div class="photo photo--checkout" role="img" aria-label="Photo of a supermarket checkout card terminal with blurred shelves behind"></div>
  <div class="photo-rule"></div>
  <h1 class="title-slide__title">Title here</h1>
  <div class="title-slide__brand">Kelvanta</div>
</section>

<section class="slide slide--agenda">
  <h2 class="heading">AGENDA</h2>
  <div class="agenda-item" style="left:35px;top:55px">
    <div class="agenda-item__title"><span class="agenda-item__num">1</span>Title Here</div>
    <ul><li>Lorem ipsum dolor sit amet, consectetur</li><li>Lorem ipsum dolor sit amet, consectetur</li><li>Lorem ipsum dolor sit amet, consectetur</li></ul>
  </div>
  <div class="agenda-item" style="left:35px;top:125px">
    <div class="agenda-item__title"><span class="agenda-item__num">2</span>Title Here</div>
    <ul><li>Lorem ipsum dolor sit amet, consectetur</li><li>Lorem ipsum dolor sit amet, consectetur</li></ul>
  </div>
  <div class="agenda-item agenda-item--muted" style="left:35px;top:191px">
    <div class="agenda-item__title"><span class="agenda-item__num">3</span>Title Here</div>
    <ul><li>Lorem ipsum dolor sit amet, consectetur</li><li>Lorem ipsum dolor sit amet, consectetur</li><li>Lorem ipsum dolor sit amet, consectetur</li></ul>
  </div>
  <div class="agenda-item" style="left:273px;top:55px">
    <div class="agenda-item__title"><span class="agenda-item__num">4</span>Title Here</div>
    <ul><li>Lorem ipsum dolor sit amet, consectetur</li><li>Lorem ipsum dolor sit amet, consectetur</li><li>Lorem ipsum dolor sit amet, consectetur</li></ul>
  </div>
  <div class="agenda-item" style="left:273px;top:125px">
    <div class="agenda-item__title"><span class="agenda-item__num">5</span>Title Here</div>
    <ul><li>Lorem ipsum dolor sit amet, consectetur</li><li>Lorem ipsum dolor sit amet, consectetur</li></ul>
  </div>
  <div class="agenda-item" style="left:273px;top:191px">
    <div class="agenda-item__title"><span class="agenda-item__num">6</span>Title Here</div>
    <ul><li>Lorem ipsum dolor sit amet, consectetur</li><li>Lorem ipsum dolor sit amet, consectetur</li><li>Lorem ipsum dolor sit amet, consectetur</li></ul>
  </div>
  <p class="agenda-note">From this economically sustainable platform, we will examine the disruption of other market segments by further leveraging the elements that make us successful.</p>
  <footer class="footer"><span class="footer__brand">Kelvanta</span><span class="footer__url">www.kelvanta.net</span></footer>
</section>

<section class="slide slide--about">
  <h2 class="heading">ABOUT Kelvanta</h2>
  <svg class="about__mark" width="94" height="94" viewBox="0 0 94 94" aria-hidden="true">
    <circle cx="47" cy="47" r="45" fill="none" stroke="var(--brand-blue)" stroke-width="3"/>
  </svg>
  <div class="about__text">
    <p>Lorem ipsum dolor sit amet, consectetur adipisicing elit, sed do eiusmod tempor incididunt ut labore et dolore magna aliqua. Ut enim ad minim veniam, quis nostrud exercitation ullamco laboris nisi ut. aliquip ex ea commodo consequat. Duis aute irure dolor in reprehenderit in voluptate velit esse cillum dolore eu fugiat nulla pariatur. Excepteur sint occaecat cupidatat non proident, sunt in culpa qui officia deserunt mollit anim id est laborum commodo consequat. Duis aute irure dolor in reprehenderit in voluptate.</p>
    <p>Velit esse cillum dolore eu fugiat nulla pariatur. Excepteur sint occaecat cupidatat non proident, sunt in culpa qui officia deserunt mollit anim id est laborumcommodo consequat. Duis aute irure dolor in reprehenderit velit esse cillum dolore eu fugiat nulla pariatur. Excepteur sint occaecat cupidatat non proident, sunt in culpa qui officia deserunt mollit anim id est laborum.</p>
  </div>
  <footer class="footer"><span class="footer__brand">Kelvanta</span><span class="footer__url">www.kelvanta.net</span></footer>
</section>

<section class="slide slide--content">
  <h2 class="heading">TITLE HERE</h2>
  <div class="subheading">Sub-Title Here</div>
  <div class="feature-icon feature-icon--team" role="img" aria-label="Team icon showing two people"></div>
  <div class="feature-icon feature-icon--idea" role="img" aria-label="Idea icon showing a glowing light bulb"></div>
  <div class="feature-icon feature-icon--process" role="img" aria-label="Process icon showing a gear"></div>
  <p class="feature-text" style="left:48px">Lorem ipsum dolor sit amet, consectetur adipisicing elit, sed do eiusmod tempor incidi dunt ut labore et dolore magna aliqua. Ut enim ad minim veniam, quis nostrud exercita tion ullamco laboris nisi ut.</p>
  <p class="feature-text" style="left:192px">Lorem ipsum dolor sit amet, consectetur adipisicing elit, sed do eiusmod tempor incidi dunt ut labore et dolore magna aliqua. Ut enim ad minim veniam, quis nostrud exercita tion ullamco laboris nisi ut.</p>
  <p class="feature-text" style="left:339px">Lorem ipsum dolor sit amet, consectetur adipisicing elit, sed do eiusmod tempor incidi dunt ut labore et dolore magna aliqua. Ut enim ad minim veniam, quis nostrud exercita tion ullamco laboris nisi ut.</p>
  <footer class="footer"><span class="footer__brand">Kelvanta</span><span class="footer__url">www.kelvanta.net</span></footer>
</section>

<section class="slide slide--blank">
  <h2 class="heading">BLANK PAGE</h2>
  <div class="subheading">Lorem ipsum dolor sit amet, consectetur dolore adipisicing elit.</div>
  <div class="profile-photo" style="left:84px" role="img" aria-label="Profile placeholder for a team member"></div>
  <div class="profile-photo" style="left:300px" role="img" aria-label="Profile placeholder for a team member"></div>
  <p class="profile-text" style="left:50px">Lorem ipsum dolor sit amet, consectetur dolore adipisicing elit, sed do eiusmod tempor incidi et dunt ut labore et dolore magnaaliqua. Ut enim ad minim veniam, quis nostrud exercitation ullamco laboris nisi ut.</p>
  <p class="profile-text" style="left:267px">Lorem ipsum dolor sit amet, consectetur dolore adipisicing elit, sed do eiusmod tempor incidi et dunt ut labore et dolore magnaaliqua. Ut enim ad minim veniam, quis nostrud exercitation ullamco laboris nisi ut.</p>
  <footer class="footer"><span class="footer__brand">Kelvanta</span><span class="footer__url">www.kelvanta.net</span></footer>
</section>

<section class="slide slide--thanks">
  <h2 class="thanks__title">THANK YOU</h2>
  <div class="thanks__url">www.kelvanta.net</div>
  <div class="photo photo--scanner" role="img" aria-label="Photo of a checkout counter with a barcode scanner and conveyor belt"></div>
</section>

</body>
</html>
```